Commit To Be The Best! - Marketing, Training, Managment for Multifamily Professionals

Flyer for training event. I have to be able to edit location, times, speakers, cost,
We will have 2 to 4 speakers for each event. Each event may have a different topic relating to the main topic (Marketing, Training, Management). The idea is to get as many people to open or pick up the fly and say "I have to attend" this seminar. We are the experts in the industry and want to portray this with the flyer. Each speaker will have a topic and a certain amount of time. Each topic will be different.
Updates

Project Deadline Extended
Reason: I apologize for the new design deadline. I've been traveling extensively for work and unable to view submissions. Currently I am not traveling and able to dedicate time to view all of the wonderful submissions. I'm looking forward to selecting one. Thank you all for your understanding.

Target Market(s)

Multifamily - Apartment Communities, Owners, Apartment Associations, Leasing Agents, Marketing Directors, Managers, Presidents,

Industry/Entity Type

Marketing

Colors

Designer to choose colors to be used in the design.

Requirements
Must have
• Editable flyer. I have to be able to edit; location, times/date, speaker, cost, description.
• Sponsored by Volt Harbor Power attached Logo for VHP
Nice to have
• Spot for photo of each speaker (2-4) speaker

```html
<!DOCTYPE html>
<html lang="en">
<head>
<meta charset="utf-8">
<title>Training Event Flyer – Sponsored by Volt Harbor Power</title>
<link href="https://fonts.googleapis.com/css2?family=Lato:wght@400;700;900&display=swap" rel="stylesheet">
<style>
  :root{
    --page-bg:#c8ccd6;
    --paper:#ffffff;
    --magenta:#e6188c;
    --sky:#2a9fd8;
    --green:#3a9a3e;
    --navy:#2e3192;
    --yellow:#fcd000;
    --ink:#2b2b2b;
    --band:#0b0b0b;
    --portrait:#77787a;
  }
  *{margin:0;padding:0;box-sizing:border-box}
  html,body{width:1200px;height:1200px;overflow:hidden;background:var(--page-bg)}
  body{font-family:'Lato',sans-serif;color:var(--ink)}
  .flyer{position:absolute;left:203px;top:43px;width:794px;height:1114px;background:var(--paper);overflow:hidden;box-shadow:0 6px 18px rgba(0,0,0,.15)}
  .block{position:absolute}
  .block--magenta{left:43px;top:13px;width:61px;height:135px;background:var(--magenta)}
  .block--sky{left:116px;top:102px;width:102px;height:46px;background:var(--sky)}
  .block--green{left:571px;top:314px;width:152px;height:41px;background:var(--green)}
  .block--yellow{left:56px;top:644px;width:41px;height:152px;background:var(--yellow);z-index:2}
  .block--navy{left:667px;top:926px;width:127px;height:41px;background:var(--navy);z-index:2}

  .sponsor{position:absolute;left:375px;top:62px;display:flex;align-items:center;gap:14px}
  .sponsor__name{font-weight:900;font-size:64px;letter-spacing:-1px;color:#111}
  .sponsor__mark{width:22px;height:22px;background:var(--magenta)}

  .photo{position:absolute}
  .photo--room{left:43px;top:158px;width:508px;height:196px;background:linear-gradient(180deg,#e9e6df 0%,#d3cfc6 45%,#5b524c 80%,#3d3733 100%)}
  .photo--audience{left:571px;top:33px;width:200px;height:264px;background:linear-gradient(160deg,#2d9cb3 0%,#1b6f86 45%,#0e3a4c 100%)}
  .photo--speaker{width:238px;height:210px;background:var(--portrait)}
  .photo--speaker-one{left:43px;top:523px}
  .photo--speaker-two{left:508px;top:734px}

  .headline{position:absolute;left:0;width:794px;text-align:center}
  .headline__kicker{top:368px;font-size:36px;font-weight:400;color:#333}
  .headline__main{top:415px;font-size:72px;font-weight:900;color:var(--navy);letter-spacing:1px}

  .speaker-label{position:absolute;height:40px;font-size:23px;font-weight:700;color:#111;display:flex;align-items:center}
  .speaker-label--green{left:312px;top:533px;width:239px;padding-left:10px;background:linear-gradient(90deg,var(--green) 0%,var(--green) 45%,rgba(58,154,62,0) 100%)}
  .speaker-label--blue{left:254px;top:764px;width:236px;justify-content:flex-end;padding-right:14px;background:linear-gradient(90deg,rgba(42,159,216,0) 0%,var(--sky) 60%,var(--sky) 100%)}

  .bio{position:absolute;width:444px;font-size:11.2px;line-height:14px;color:#333}
  .bio p+p{margin-top:6px}
  .bio--one{left:315px;top:584px}
  .bio--two{left:43px;top:820px;text-align:right}

  .info-band{position:absolute;left:0;top:985px;width:794px;height:96px;background:var(--band);display:flex;align-items:center;color:#fff;font-size:21px}
  .info-item{position:absolute;display:flex;align-items:center;gap:16px;line-height:25px}
  .info-item--date{left:54px}
  .info-item--time{left:328px}
  .info-item--cost{left:556px}
  .info-item svg{width:44px;height:44px;flex:none}

  .color-strip{position:absolute;left:0;top:1096px;width:794px;height:18px;display:flex}
  .color-strip span{height:100%}
</style>
</head>
<body>
<main class="flyer">
  <div class="block block--magenta"></div>
  <div class="block block--sky"></div>

  <div class="sponsor" aria-label="Sponsored by Volt Harbor Power">
    <span class="sponsor__name">VHP</span>
    <span class="sponsor__mark"></span>
  </div>

  <div class="photo photo--room" role="img" aria-label="Photo of a seminar room with attendees facing a projection screen"></div>
  <div class="photo photo--audience" role="img" aria-label="Blue-toned photo of an audience at a conference"></div>
  <div class="block block--green"></div>

  <h2 class="headline headline__kicker">Lorem Ipsum is simply</h2>
  <h1 class="headline headline__main">DUMMY TEXT</h1>

  <div class="photo photo--speaker photo--speaker-one" role="img" aria-label="Portrait of the first speaker"></div>
  <div class="block block--yellow"></div>
  <div class="speaker-label speaker-label--green">Speaker Name</div>
  <div class="bio bio--one">
    <p>Lorem Ipsum is simply dummy text of the printing and typesetting industry. Lorem Ipsum has been the industry's standard dummy text ever since the 1500s, when an unknown printer took a galley of type and scrambled it to make a type specimen book. It has survived not only five centuries, but also the leap into electronic typesetting, remaining essentially unchanged.</p>
    <p>It was popularised in the 1960s with the release of Letraset sheets containing Lorem Ipsum passages, and more recently with desktop publishing software like Aldus PageMaker including versions of Lorem Ipsum.</p>
  </div>

  <div class="speaker-label speaker-label--blue">Speaker Name</div>
  <div class="bio bio--two">
    <p>Lorem Ipsum is simply dummy text of the printing and typesetting industry. Lorem Ipsum has been the industry's standard dummy text ever since the 1500s, when an unknown printer took a galley of type and scrambled it to make a type specimen book. It has survived not only five centuries, but also the leap into electronic typesetting, remaining essentially unchanged.</p>
    <p>It was popularised in the 1960s with the release of Letraset sheets containing Lorem Ipsum passages, and more recently with desktop publishing software like Aldus PageMaker including versions of Lorem Ipsum.</p>
  </div>
  <div class="photo photo--speaker photo--speaker-two" role="img" aria-label="Portrait of the second speaker"></div>
  <div class="block block--navy"></div>

  <section class="info-band">
    <div class="info-item info-item--date">
      <svg viewBox="0 0 44 44" fill="none" stroke="#fcd000" stroke-width="2.6">
        <rect x="5" y="8" width="34" height="30" rx="2"/>
        <line x1="5" y1="16" x2="39" y2="16"/>
        <line x1="13" y1="4" x2="13" y2="11"/><line x1="31" y1="4" x2="31" y2="11"/>
        <g fill="#fcd000" stroke="none">
          <rect x="10" y="20" width="4" height="4"/><rect x="17" y="20" width="4" height="4"/><rect x="24" y="20" width="4" height="4"/><rect x="31" y="20" width="4" height="4"/>
          <rect x="10" y="28" width="4" height="4"/><rect x="17" y="28" width="4" height="4"/><rect x="24" y="28" width="4" height="4"/><rect x="31" y="28" width="4" height="4"/>
        </g>
      </svg>
      <span>Lorem Ipsum is a<br>dummy text</span>
    </div>
    <div class="info-item info-item--time">
      <svg viewBox="0 0 44 44" fill="none" stroke="#fcd000" stroke-width="2.8" stroke-linecap="round">
        <path d="M36 14 A17 17 0 1 1 26 6"/>
        <polyline points="13,23 20,30 36,8"/>
      </svg>
      <span>Lorem Ipsum</span>
    </div>
    <div class="info-item info-item--cost">
      <svg viewBox="0 0 44 44" fill="none" stroke="#fcd000" stroke-width="2.8">
        <circle cx="22" cy="22" r="18"/>
        <path d="M28 15c-2-2-10-3-11 2s11 4 11 9-9 4-12 1" stroke-linecap="round"/>
        <line x1="22" y1="10" x2="22" y2="34"/>
      </svg>
      <span>Lorem Ipsum</span>
    </div>
  </section>

  <div class="color-strip">
    <span style="width:246px;background:var(--green)"></span>
    <span style="width:163px;background:var(--sky)"></span>
    <span style="width:106px;background:var(--navy)"></span>
    <span style="width:97px;background:var(--yellow)"></span>
    <span style="width:182px;background:var(--magenta)"></span>
  </div>
</main>
</body>
</html>
```